brolvin business card design so that it looks better

need a new business card designed. use our website, brolvix.example for example. I attached an example of a previous card we had and liked. this is for law enforcement and we have attached a previous business card as an example. This site forces me to select color and font, ignore those as I picked stuff just to get this completed.

Target Market(s)

law enforcement, local government

Contact Information for Business Card

see the attached example and our website

Font styles to use
Serif

```html
<!DOCTYPE html>
<html lang="en">
<head>
<meta charset="utf-8">
<title>Brolvin Business Card</title>
<link rel="stylesheet" href="https://fonts.googleapis.com/css2?family=Roboto:wght@300;400;700&display=swap">
<style>
  :root {
    --page-bg: #3b3c3f;
    --card-dark: #231f20;
    --card-blue: #14558a;
    --ink-light: #ffffff;
    --ink-soft: #dfe8f1;
    --band: #ffffff;
  }
  * { box-sizing: border-box; margin: 0; padding: 0; }
  html, body {
    width: 1200px; height: 900px; overflow: hidden;
    background: var(--page-bg);
    font-family: "Roboto", Arial, sans-serif;
  }
  .sheet {
    position: relative; width: 1200px; height: 900px;
    display: flex; flex-direction: column; align-items: center;
    justify-content: center; gap: 40px;
  }
  .card {
    position: relative; width: 700px; height: 400px;
    border-radius: 24px; overflow: hidden;
  }
  .card--back { background: var(--card-dark); }
  .card--front { background: var(--card-blue); }
  .wordmark {
    font-family: "Roboto", Arial, sans-serif;
    font-weight: 300; color: var(--ink-light);
    letter-spacing: 0.08em; line-height: 1;
    position: absolute; left: 0; right: 0; text-align: center;
  }
  .card--back .wordmark { top: 160px; font-size: 80px; }
  .card--front .wordmark { top: 62px; font-size: 72px; }
  .identity {
    position: absolute; left: 0; width: 318px; top: 192px;
    text-align: right; color: var(--ink-light);
  }
  .identity__name { font-size: 21px; font-weight: 700; }
  .identity__title { font-size: 15px; font-weight: 400; color: var(--ink-soft); margin-top: 2px; }
  .divider {
    position: absolute; left: 338px; top: 172px;
    width: 1px; height: 86px; background: var(--ink-soft);
  }
  .contacts {
    position: absolute; left: 360px; top: 170px;
    list-style: none; color: var(--ink-light); font-size: 14px;
  }
  .contacts__item { display: flex; align-items: center; gap: 12px; height: 30px; }
  .contacts__icon { width: 15px; height: 15px; flex: none; }
  .band {
    position: absolute; left: 0; right: 0; top: 296px; height: 58px;
    background: var(--band);
  }
  .band__address {
    position: absolute; left: 0; right: 0; top: 8px;
    text-align: center; font-size: 15px; color: var(--card-blue);
  }
</style>
</head>
<body>
<main class="sheet">
  <section class="card card--back" aria-label="Card back">
    <div class="wordmark">BROLVIN</div>
  </section>

  <section class="card card--front" aria-label="Card front">
    <div class="wordmark">BROLVIN</div>

    <div class="identity">
      <div class="identity__name">Dana Merrow</div>
      <div class="identity__title">President</div>
    </div>

    <div class="divider"></div>

    <ul class="contacts">
      <li class="contacts__item">
        <svg class="contacts__icon" viewBox="0 0 16 16" aria-hidden="true">
          <path d="M4 1.5l2.2 3-1.4 1.6c.8 1.8 2.3 3.3 4.1 4.1l1.6-1.4 3 2.2-1.2 2.5C7 13.3 2.7 9 2.2 3.1z" fill="#fff"/>
        </svg>
        <span>555.014.2270</span>
      </li>
      <li class="contacts__item">
        <svg class="contacts__icon" viewBox="0 0 16 16" aria-hidden="true">
          <rect x="1.5" y="3.5" width="13" height="9" fill="none" stroke="#fff" stroke-width="1.2"/>
          <path d="M1.5 3.5L8 9l6.5-5.5" fill="none" stroke="#fff" stroke-width="1.2"/>
        </svg>
        <span>info@brolvix.example</span>
      </li>
      <li class="contacts__item">
        <svg class="contacts__icon" viewBox="0 0 16 16" aria-hidden="true">
          <circle cx="8" cy="8" r="6.5" fill="none" stroke="#fff" stroke-width="1.2"/>
          <ellipse cx="8" cy="8" rx="2.8" ry="6.5" fill="none" stroke="#fff" stroke-width="1"/>
          <path d="M1.5 8h13M2.5 5h11M2.5 11h11" stroke="#fff" stroke-width="1"/>
        </svg>
        <span>brolvix.example</span>
      </li>
    </ul>

    <div class="band">
      <p class="band__address">4120 Larkspur Avenue Easton, TX 70010</p>
    </div>
  </section>
</main>
</body>
</html>
```